Criação de Cartao de Visita para Consultoria de Negócios
" Coaching para altos executivos com foco em desenvolvimento de liderança, coaching de carreira e detalhamento de perfil, coaching para autoconhecimento, programas de orientação vocacional e inteligência emocional. "

```html
<!DOCTYPE html>
<html lang="pt-BR">
<head>
<meta charset="UTF-8">
<title>Aurora Coaching – Cartão de Visita</title>
<link rel="stylesheet" href="https://fonts.googleapis.com/css2?family=Josefin+Sans:wght@300;400&family=Montserrat:wght@400;600;700&display=swap">
<style>
  :root {
    --bg: #e8e8ea;
    --card: #ffffff;
    --blue: #3d9fe2;
    --blue-deep: #2f8fd4;
    --gold: #e2b04a;
    --orange: #f29422;
    --grey: #8c8c8c;
    --white: #ffffff;
  }
  * { margin: 0; padding: 0; box-sizing: border-box; }
  html, body { width: 1200px; height: 1200px; overflow: hidden; }
  body { background: var(--bg); position: relative; font-family: "Montserrat", sans-serif; }

  .card {
    position: absolute;
    left: 220px;
    width: 760px;
    height: 434px;
    border-radius: 30px;
    overflow: hidden;
    background: var(--card);
    box-shadow: 0 10px 30px rgba(0,0,0,0.10);
  }
  .card--front { top: 110px; }
  .card--back { top: 640px; }
  .card svg.card-shapes { position: absolute; inset: 0; }

  .brand {
    position: absolute;
    left: 0; right: 0;
    top: 170px;
    display: flex;
    align-items: center;
    justify-content: center;
    gap: 14px;
  }
  .brand-dot { width: 22px; height: 22px; border-radius: 50%; background: var(--orange); }
  .brand-name {
    font-family: "Josefin Sans", sans-serif;
    font-weight: 300;
    font-size: 46px;
    letter-spacing: 2px;
    color: var(--blue);
    text-transform: uppercase;
  }
  .brand-tagline {
    position: absolute;
    left: 0; right: 0;
    top: 236px;
    text-align: center;
    font-size: 11px;
    letter-spacing: 3px;
    color: var(--grey);
    text-transform: uppercase;
  }

  .contact-name {
    position: absolute;
    left: 60px;
    top: 150px;
    font-weight: 700;
    font-size: 33px;
    color: var(--white);
    letter-spacing: 1px;
    white-space: nowrap;
  }
  .contact-list {
    position: absolute;
    left: 60px;
    top: 212px;
    list-style: none;
  }
  .contact-item {
    display: flex;
    align-items: flex-start;
    gap: 12px;
    margin-bottom: 12px;
    color: var(--white);
    font-size: 12px;
    font-weight: 600;
    text-transform: uppercase;
    letter-spacing: 0.4px;
    line-height: 1.45;
    white-space: nowrap;
  }
  .contact-icon { width: 20px; height: 20px; flex: none; }

  .back-brand {
    position: absolute;
    left: 475px;
    width: 240px;
    top: 86px;
    text-align: center;
  }
  .back-brand .brand-name { font-size: 30px; line-height: 1.1; }
  .back-brand .brand-dot { width: 16px; height: 16px; margin: 0 auto 12px; }
  .back-web {
    margin-top: 12px;
    font-size: 9px;
    letter-spacing: 1.6px;
    color: var(--grey);
    text-transform: uppercase;
  }
</style>
</head>
<body>

  <section class="card card--front" aria-label="Frente do cartão">
    <svg class="card-shapes" width="760" height="434" viewBox="0 0 760 434">
      <path d="M0 250 Q46 330 22 434 L0 434 Z" fill="var(--orange)"/>
    </svg>
    <div class="brand">
      <span class="brand-dot"></span>
      <span class="brand-name">Aurora Coaching</span>
    </div>
    <p class="brand-tagline">Liderança · Carreira · Autoconhecimento · Vocação</p>
  </section>

  <section class="card card--back" aria-label="Verso do cartão">
    <svg class="card-shapes" width="760" height="434" viewBox="0 0 760 434">
      <defs>
        <linearGradient id="blueFade" x1="0" y1="0" x2="0" y2="1">
          <stop offset="0" stop-color="var(--blue)"/>
          <stop offset="1" stop-color="var(--blue-deep)"/>
        </linearGradient>
      </defs>
      <rect width="760" height="434" fill="url(#blueFade)"/>
      <circle cx="640" cy="120" r="240" fill="var(--gold)"/>
      <circle cx="640" cy="120" r="218" fill="var(--card)"/>
      <path d="M0 250 Q40 330 18 434 L0 434 Z" fill="var(--orange)"/>
    </svg>

    <h2 class="contact-name">LOREM IPSUM</h2>
    <ul class="contact-list">
      <li class="contact-item">
        <svg class="contact-icon" viewBox="0 0 24 24" fill="none" stroke="#fff" stroke-width="1.8"><circle cx="12" cy="12" r="10.5"/><path d="M8.5 7.5l2 2-1 1.5a6 6 0 0 0 3.5 3.5l1.5-1 2 2-1 1.5c-3.5 0-8-4.5-8-8z" fill="#fff" stroke="none"/></svg>
        <span>(19) 90000-0000</span>
      </li>
      <li class="contact-item">
        <svg class="contact-icon" viewBox="0 0 24 24" fill="none" stroke="#fff" stroke-width="1.8"><rect x="3" y="6" width="18" height="12" rx="1.5"/><path d="M3.5 7l8.5 6 8.5-6"/></svg>
        <span>contato@auroracoaching.com.br</span>
      </li>
      <li class="contact-item">
        <svg class="contact-icon" viewBox="0 0 24 24" fill="none" stroke="#fff" stroke-width="1.8"><circle cx="12" cy="12" r="9"/></svg>
        <span>/auroracoaching</span>
      </li>
      <li class="contact-item">
        <svg class="contact-icon" viewBox="0 0 24 24" fill="#fff"><path d="M12 2a7 7 0 0 0-7 7c0 5 7 13 7 13s7-8 7-13a7 7 0 0 0-7-7zm0 9.5A2.5 2.5 0 1 1 12 6.5a2.5 2.5 0 0 1 0 5z"/></svg>
        <span>Rua das Acácias, 120 Sala 4,<br>Campinas - SP, CEP 13010-000</span>
      </li>
    </ul>

    <div class="back-brand">
      <div class="brand-dot"></div>
      <div class="brand-name">Aurora Coaching</div>
      <div class="back-web">www.auroracoaching.com.br</div>
    </div>
  </section>

</body>
</html>
```